Camp Maplebrook Summer Programs Postcard

We need a postcard design for summer 2017 programs. Camp Maplebrook offers nine weeks of day camp and one week of overnight camp. We are a Christian summer camp. We offer lots of activities like swimming, archery, rock wall, zipline, sports, crafts, drama and more. We want to showcase the activities we offer. The design should communicate outdoor fun and friendship. We want to focus on high quality photos that reflect the activities we offer.

Target Market(s)

Elementary age children/parents

Industry/Entity Type

Childcare

Font styles to use
Serif

Requirements
Must have
• Camp Maplebrook "Christian Camping Since 1952"
• Day Camp 2017 "Courageous Campers"
• June 19 - August 18
• $130 per week
• Mon-Fri 8 am to 4 pm. Open to all kids entering grades 1 to 8. Day camp is chock full of activities like swimming, rock wall, archery, zipline, sports, campfires and much more! Daily lunch and snack included. Before and after-care available at an extra rate.
• Overnight Camp 2017
• July 16 - 22
• $325
• Open to all kids ages 8 to 14. Spend the week making new friends, sleeping in cabins, climbing the rock wall and ziplining under the stars! Our special guest speaker will lead twice daily chapel sessions that will challenge campers to grow in their faith.
• Register and pay for 7 weeks by May 1st, get 2 FREE!
• Website: www.maplebrook-example.org
• Address: 41 Cedar Vale Rd. Lisford, NH 03999
• Phone: 603-555-0148

```html
<!DOCTYPE html>
<html lang="en">
<head>
<meta charset="utf-8">
<title>Camp Maplebrook Summer Programs Postcard</title>
<link rel="stylesheet" href="https://fonts.googleapis.com/css2?family=Tinos:wght@400;700&display=swap">
<style>
  :root {
    --backdrop: #8e8e8e;
    --card: #ffffff;
    --brown: #744b27;
    --red: #c0272d;
    --white: #ffffff;
    --photo-green: #6f8f4e;
    --photo-sky: #9db8c6;
    --photo-warm: #c98a5e;
    --photo-water: #5d7f86;
  }
  * { box-sizing: border-box; margin: 0; padding: 0; }
  html, body { width: 1189px; height: 1200px; overflow: hidden; }
  body {
    position: relative;
    background: var(--backdrop);
    font-family: "Tinos", "Times New Roman", serif;
  }
  .postcard {
    position: absolute;
    left: 226px;
    width: 734px;
    height: 490px;
    background: var(--card);
    box-shadow: 2px 3px 5px rgba(0,0,0,.35);
  }
  .postcard--front { top: 78px; }
  .postcard--back { top: 637px; }

  .photo { position: absolute; }
  .photo--games { left: 7px; top: 6px; width: 341px; height: 256px; background: linear-gradient(160deg, #7f8a6a, var(--photo-green) 55%, #5c7a3c); }
  .photo--smile { left: 355px; top: 6px; width: 166px; height: 126px; background: linear-gradient(150deg, #8f9a6c, #b66a4a); }
  .photo--friends { left: 355px; top: 137px; width: 166px; height: 125px; background: linear-gradient(150deg, #d98a4c, var(--photo-warm)); }
  .photo--climb { left: 527px; top: 6px; width: 200px; height: 256px; background: linear-gradient(90deg, #6f9150, #a8aca2 60%, #c2bfb2); }

  .promo-band {
    position: absolute; left: 0; top: 269px; width: 100%; height: 37px;
    background: var(--brown); color: var(--white);
    font-weight: 700; font-size: 18px; letter-spacing: .2px;
    display: flex; align-items: center; justify-content: center;
  }
  .day-camp-title {
    position: absolute; left: 20px; top: 325px; width: 398px;
    text-align: center; color: var(--brown); font-weight: 700;
  }
  .day-camp-title .line { display: block; font-size: 29px; line-height: 36px; }
  .day-camp-title .dates { display: block; font-size: 18px; line-height: 22px; margin-top: 2px; }

  .price-badge { position: absolute; }
  .price-badge--week { left: 574px; top: 318px; width: 106px; height: 106px; }
  .price-badge--overnight { left: 298px; top: 20px; width: 60px; height: 60px; }

  .details-band {
    position: absolute; left: 0; top: 439px; width: 100%; height: 49px;
    background: var(--brown); color: var(--white);
    font-size: 12.8px; line-height: 16px; text-align: center;
    display: flex; align-items: center; justify-content: center; padding: 0 18px;
  }

  .overnight-title { position: absolute; left: 16px; top: 16px; color: var(--red); font-weight: 400; }
  .overnight-title .name { display: block; font-size: 16.5px; line-height: 20px; }
  .overnight-title .dates { display: block; font-size: 13px; line-height: 16px; }
  .overnight-copy {
    position: absolute; left: 16px; top: 88px; width: 356px;
    color: var(--brown); font-size: 13px; line-height: 16px; text-align: justify;
  }
  .thumb { position: absolute; width: 111px; height: 111px; border-radius: 6px; }
  .thumb--boy { left: 16px; top: 167px; background: linear-gradient(150deg, #7fa06a, #c7b7a4); }
  .thumb--girl { left: 135px; top: 167px; background: linear-gradient(150deg, #d8d2c8, #e6935c); }
  .thumb--wall { left: 256px; top: 167px; background: linear-gradient(90deg, var(--photo-sky), #6c9b52); }
  .thumb--boat { left: 16px; top: 287px; background: linear-gradient(180deg, var(--photo-water), #d2b23a); }

  .camp-name {
    position: absolute; left: 146px; top: 318px; width: 220px;
    text-align: center; color: var(--brown);
  }
  .camp-name .wordmark { display: block; font-size: 27px; font-weight: 700; line-height: 32px; }
  .camp-name .tagline {
    display: block; margin-top: 12px;
    font-size: 13px; font-weight: 400; line-height: 16px;
  }
  .contact-band {
    position: absolute; left: 0; top: 412px; width: 367px; height: 76px;
    background: var(--brown); color: var(--white);
    font-size: 13px; line-height: 16px; padding: 15px 16px 0;
    font-style: normal;
  }
  .contact-band strong { font-weight: 700; }
</style>
</head>
<body>
  <section class="postcard postcard--front">
    <div class="photo photo--games" role="img" aria-label="Campers in pinnies running across a grassy field with a flying disc"></div>
    <div class="photo photo--smile" role="img" aria-label="Smiling camper sitting outdoors"></div>
    <div class="photo photo--friends" role="img" aria-label="Two girls posing together at camp"></div>
    <div class="photo photo--climb" role="img" aria-label="Child in a helmet and harness climbing the rock wall"></div>

    <div class="promo-band">REGISTER AND PAY FOR 7 WEEKS BY MAY 1ST, GET 2 FREE!</div>

    <h1 class="day-camp-title">
      <span class="line">DAY CAMP 2017</span>
      <span class="line">COURAGEOUS CAMPERS</span>
      <span class="dates">JUNE 19 - AUGUST 18</span>
    </h1>

    <svg class="price-badge price-badge--week" viewBox="0 0 106 106" aria-label="$130 per week">
      <circle cx="53" cy="53" r="47" fill="#744b27"/>
      <circle cx="53" cy="53" r="49" fill="none" stroke="#744b27" stroke-width="6" stroke-dasharray="3 2.2"/>
      <circle cx="53" cy="53" r="41" fill="none" stroke="#fff" stroke-width=".8" stroke-dasharray="1.5 1.5"/>
      <g transform="rotate(-15 53 53)" fill="#fff" font-family="Tinos, serif" text-anchor="middle">
        <text x="53" y="60" font-size="34">$130</text>
        <text x="56" y="75" font-size="11" font-weight="700" letter-spacing=".5">PER WEEK</text>
      </g>
    </svg>

    <p class="details-band">Mon-Fri 8 am to 4 pm. Open to all kids entering grades 1 to 8. Day camp is chock full of activities like swimming, rock wall, archery zipline, sports, campfires and much more! Daily lunch and snack included. Before and after-care available at an extra rate.</p>
  </section>

  <section class="postcard postcard--back">
    <h2 class="overnight-title">
      <span class="name">Overnight Camp 2017</span>
      <span class="dates">July 16 - 22</span>
    </h2>

    <svg class="price-badge price-badge--overnight" viewBox="0 0 60 60" aria-label="$325">
      <circle cx="30" cy="30" r="26" fill="#744b27"/>
      <circle cx="30" cy="30" r="27.5" fill="none" stroke="#744b27" stroke-width="4" stroke-dasharray="2 1.6"/>
      <circle cx="30" cy="30" r="23" fill="none" stroke="#fff" stroke-width=".6" stroke-dasharray="1 1"/>
      <text x="30" y="35" transform="rotate(-15 30 30)" fill="#fff" font-family="Tinos, serif" font-size="16" text-anchor="middle">$325</text>
    </svg>

    <p class="overnight-copy">Open to all kids ages 8 to 14. Spend the week making new friends, sleeping in cabins, climbing the rock wall and ziplining under the stars! Our special guest speaker will lead twice daily chapel sessions that will challenge campers to grow in their faith.</p>

    <div class="thumb thumb--boy" role="img" aria-label="Grinning boy outdoors at camp"></div>
    <div class="thumb thumb--girl" role="img" aria-label="Smiling girl at a camp activity"></div>
    <div class="thumb thumb--wall" role="img" aria-label="Young climber on the rock wall"></div>
    <div class="thumb thumb--boat" role="img" aria-label="Campers in life jackets on a yellow pedal boat"></div>

    <div class="camp-name">
      <span class="wordmark">Camp Maplebrook</span>
      <span class="tagline">Christian Camping Since 1952</span>
    </div>

    <address class="contact-band">
      <strong>Website:</strong> www.maplebrook-example.org<br>
      <strong>Address:</strong> 41 Cedar Vale Rd. Lisford, NH 03999<br>
      <strong>Phone:</strong> 603-555-0148
    </address>
  </section>
</body>
</html>
```